Business Card Design Project - 2 sided

We need a business card design for a card having one business on each side (ie. two businesses on one card). Would like a design that incorporates logo, tagline and normal fields (name, position, address, phone).

Would also like an allowance for small font text along the bottom (text to be determined, but less than 50 characters).

NB. Attached logo for Verbica Partners has two variations - either can be used.

www.verbicapartners.com / www.kelvarho.com

```html
<!DOCTYPE html>
<html lang="en">
<head>
<meta charset="utf-8">
<title>Two-sided business card – Kelvarho / Verbica Partners</title>
<link rel="stylesheet" href="https://fonts.googleapis.com/css2?family=Source+Sans+3:wght@400;600&family=Libre+Baskerville:wght@400;700&display=swap">
<style>
  :root {
    --backdrop: #e9e6e1;
    --card-white: #ffffff;
    --card-grey: #eeeeef;
    --green: #7dc243;
    --green-light: #a8d67b;
    --navy: #2b2a7a;
    --blue: #2f7fc1;
    --ink: #2a2a2a;
    --ink-soft: #555555;
    --ring: #d9d9e6;
  }
  * { box-sizing: border-box; margin: 0; padding: 0; }
  html, body { width: 1200px; height: 900px; overflow: hidden; }
  body {
    background: var(--backdrop);
    display: flex;
    align-items: center;
    justify-content: center;
    gap: 40px;
  }
  .card {
    position: relative;
    width: 540px;
    height: 310px;
    overflow: hidden;
    box-shadow: 0 6px 18px rgba(0,0,0,0.18);
  }
  .icon { width: 12px; height: 12px; flex: none; }

  /* Kelvarho side */
  .card--kelvarho {
    background: var(--card-white);
    font-family: "Source Sans 3", Arial, sans-serif;
    color: var(--ink);
  }
  .card--kelvarho .edge-stripe {
    position: absolute; left: 0; right: 0; bottom: 0; height: 12px;
    background: var(--green);
  }
  .card--kelvarho .brand {
    position: absolute; left: 36px; top: 42px;
    display: flex; align-items: center; gap: 10px;
  }
  .card--kelvarho .brand-dot {
    width: 34px; height: 34px; border-radius: 50%; background: var(--green);
  }
  .card--kelvarho .brand-name {
    font-size: 38px; font-weight: 600; color: var(--blue); letter-spacing: 0.5px;
  }
  .card--kelvarho .person { position: absolute; left: 36px; top: 132px; }
  .card--kelvarho .person-name { font-size: 19px; font-weight: 600; color: var(--blue); }
  .card--kelvarho .person-role { font-size: 14px; color: var(--ink-soft); margin-top: 2px; }
  .card--kelvarho .contact {
    position: absolute; left: 36px; top: 196px;
    list-style: none; font-size: 14px; line-height: 21px;
  }
  .contact li { display: flex; align-items: center; gap: 7px; }
  .card--kelvarho .icon { fill: var(--blue); }
  .card--kelvarho .addresses {
    position: absolute; right: 36px; top: 150px;
    display: flex; gap: 34px; font-size: 13px; line-height: 18px; color: var(--ink-soft);
  }

  /* Verbica side */
  .card--verbica {
    background: var(--card-grey);
    font-family: "Libre Baskerville", Georgia, serif;
    color: var(--ink);
  }
  .card--verbica .name-band {
    position: absolute; left: 0; right: 0; top: 0; height: 56px;
    background: linear-gradient(90deg, var(--green-light) 0 28%, var(--green) 28% 100%);
    display: flex; align-items: center; padding-left: 190px; gap: 10px;
  }
  .card--verbica .person-name { font-size: 18px; font-weight: 700; color: var(--ink); }
  .card--verbica .person-role { font-size: 11px; color: var(--ink); }
  .card--verbica .edge-stripe {
    position: absolute; left: 0; right: 0; bottom: 0; height: 14px;
    background: var(--navy);
  }
  .card--verbica .ring-field {
    position: absolute; right: -30px; top: 40px; width: 240px; height: 200px;
    background: radial-gradient(circle at 55% 45%, rgba(217,217,230,0.7), rgba(238,238,239,0) 70%);
  }
  .card--verbica .brand {
    position: absolute; left: 30px; top: 88px;
    display: flex; align-items: center; gap: 10px;
  }
  .card--verbica .brand-dot {
    width: 26px; height: 26px; border-radius: 50%; background: var(--green);
  }
  .card--verbica .brand-name {
    font-size: 25px; font-weight: 400; color: var(--navy); letter-spacing: 0.5px;
  }
  .card--verbica .address {
    position: absolute; left: 30px; bottom: 44px;
    font-size: 13px; line-height: 19px;
  }
  .card--verbica .contact {
    position: absolute; right: 40px; top: 150px;
    list-style: none; font-size: 12px; line-height: 20px;
  }
  .card--verbica .icon { fill: var(--navy); }
</style>
</head>
<body>

<svg width="0" height="0" style="position:absolute">
  <defs>
    <symbol id="icon-phone" viewBox="0 0 24 24"><path d="M6.6 10.8a15 15 0 0 0 6.6 6.6l2.2-2.2c.3-.3.7-.4 1-.2 1.1.4 2.3.6 3.6.6.6 0 1 .4 1 1V20c0 .6-.4 1-1 1A17 17 0 0 1 3 4c0-.6.4-1 1-1h3.5c.6 0 1 .4 1 1 0 1.3.2 2.5.6 3.6.1.3 0 .7-.2 1z"/></symbol>
    <symbol id="icon-mail" viewBox="0 0 24 24"><path d="M2 5h20v14H2zm2 2v.5l8 5 8-5V7z"/></symbol>
    <symbol id="icon-web" viewBox="0 0 24 24"><path d="M3 3h18v18H3zm3 4v2a8 8 0 0 1 8 8h2A10 10 0 0 0 6 7zm0 4v2a4 4 0 0 1 4 4h2a6 6 0 0 0-6-6zm1 4a1 1 0 1 0 0 2 1 1 0 0 0 0-2z"/></symbol>
  </defs>
</svg>

<section class="card card--kelvarho" aria-label="Kelvarho side">
  <div class="brand">
    <span class="brand-dot"></span>
    <span class="brand-name">kelvarho</span>
  </div>
  <div class="person">
    <p class="person-name">Maren Ashdown</p>
    <p class="person-role">Manager</p>
  </div>
  <ul class="contact">
    <li><svg class="icon"><use href="#icon-phone"/></svg>+1 555-208-0147</li>
    <li><svg class="icon"><use href="#icon-mail"/></svg>support@kelvarho.com</li>
    <li><svg class="icon"><use href="#icon-web"/></svg>www.kelvarho.com</li>
  </ul>
  <div class="addresses">
    <address style="font-style:normal">PO Box 42<br>Lindale Ohio<br>44021, USA</address>
    <address style="font-style:normal">Marlow Drive<br>Seabrook, Texas<br>77586, USA</address>
  </div>
  <div class="edge-stripe"></div>
</section>

<section class="card card--verbica" aria-label="Verbica Partners side">
  <div class="ring-field" role="img" aria-label="Soft decorative overlapping rings"></div>
  <div class="name-band">
    <span class="person-name">Maren Ashdown</span>
    <span class="person-role">Manager</span>
  </div>
  <div class="brand">
    <span class="brand-dot"></span>
    <span class="brand-name">Verbica Partners</span>
  </div>
  <ul class="contact">
    <li><svg class="icon"><use href="#icon-phone"/></svg>+61 3 9400 1234</li>
    <li><svg class="icon"><use href="#icon-mail"/></svg>info@verbicapartners.com</li>
    <li><svg class="icon"><use href="#icon-web"/></svg>www.verbicapartners.com</li>
  </ul>
  <address class="address" style="font-style:normal">27 Fenwick Street<br>Kew VIC 3101<br>AUSTRALIA</address>
  <div class="edge-stripe"></div>
</section>

</body>
</html>
```